We'd like to rebrand The Ashvale Crafters & Bazaar to be a professional but community oriented market. This market will go from inside and outside, inviting locally made jewelry, clothing, house wares, knits, vintage and more. We always have buskers, coffee and dainties. This is a year- round market, so it has to work for Fall, Winter, Spring, Summer.
We'd like the words:
Local
Community
Music
and/or
Hand Made
Please, also make the dimensions 22x79.
This will a printed banner to hang at indoor and outdoor markets.
Adults in North America 20-55+
Average House-hold Budgets
House
Ashvale Crafters & Bazaar

```html
<!DOCTYPE html>
<html lang="en">
<head>
<meta charset="utf-8">
<title>Ashvale Crafters &amp; Bazaar – Banner</title>
<link rel="stylesheet" href="https://fonts.googleapis.com/css2?family=Fira+Sans:ital,wght@1,800&family=Source+Sans+3:wght@400;700&display=swap">
<style>
  :root {
    --stage: #1a1a1a;
    --green-top: #9bb922;
    --green-mid: #86b016;
    --green-low: #6ca70a;
    --green-base: #4f8a04;
    --title: #ffffff;
    --tagline: #dfe5fa;
    --tagline-shadow: rgba(40, 60, 10, 0.55);
  }
  html, body {
    margin: 0;
    padding: 0;
    overflow: hidden;
    background: var(--stage);
  }
  .canvas {
    position: relative;
    width: 1200px;
    height: 1000px;
    background: var(--stage);
    overflow: hidden;
  }
  .banner {
    position: absolute;
    left: 453px;
    top: 0;
    width: 288px;
    height: 1000px;
    background: linear-gradient(to bottom, var(--green-top) 0%, var(--green-mid) 45%, var(--green-low) 96%, var(--green-base) 100%);
  }
  .banner-title {
    position: absolute;
    left: 0;
    top: 58px;
    width: 288px;
    margin: 0;
    text-align: center;
    font-family: "Fira Sans", sans-serif;
    font-style: italic;
    font-weight: 800;
    font-size: 47px;
    line-height: 66px;
    letter-spacing: -1px;
    color: var(--title);
    text-shadow: 1px 2px 2px rgba(40, 60, 10, 0.45);
  }
  .banner-title .amp {
    display: block;
    font-size: 44px;
  }
  .tagline {
    position: absolute;
    left: 29px;
    top: 712px;
    margin: 0;
    font-family: "Source Sans 3", sans-serif;
    font-size: 31px;
    line-height: 41.5px;
    color: var(--tagline);
    text-shadow: 1px 1px 2px var(--tagline-shadow);
    list-style: none;
    padding: 0;
  }
  .tagline .strong { font-weight: 700; }
  .tagline .light { font-weight: 400; }
</style>
</head>
<body>
  <div class="canvas">
    <section class="banner" role="img" aria-label="Green vertical market banner with faint pattern of market icons: headphones, soccer balls, coffee cups, wine glasses, umbrellas, butterflies">
      <h1 class="banner-title">ASHVALE<br>CRAFTERS<span class="amp">&amp;</span>BAZAAR</h1>
      <ul class="tagline">
        <li><span class="strong">LOCAL</span><span class="light">/</span></li>
        <li><span class="light">COMMUNITY/</span></li>
        <li><span class="strong">MUSIC</span><span class="light">/AND/OR</span></li>
        <li><span class="strong">HAND MADE</span></li>
      </ul>
    </section>
  </div>
</body>
</html>
```